Need Letterhead Design & Matching Business Card

I have a logo that I love already. But the letterhead is less than appealing and boring. I'd like a design for my letterhead which I will match with business cards. Also, I'd like to have used fonts that are generally available, as my current letterhead uses a font named "SPACE" which nobody has unless they download it...so when a Word version is forwarded, it looks awful on the receiver's screed due to not having the font. That being said, modern is the look we like and are going for.

My business is "Halloran Brightmoor PC" - a law firm specializing in representing people who have suffered catastrophic injuries or death (plane, auto, train crashes etc.).

See attached letterhead, which has all of the pertinent information. My logo is also attached in various formats.

```html
<!DOCTYPE html>
<html lang="en">
<head>
<meta charset="utf-8">
<title>Halloran Brightmoor PC — Letterhead &amp; Business Cards</title>
<link href="https://fonts.googleapis.com/css2?family=Lato:wght@400;700;900&family=Montserrat:wght@500;600&family=Questrial&display=swap" rel="stylesheet">
<style>
  :root {
    --backdrop: #d2d2d2;
    --paper: #ffffff;
    --ink: #111111;
    --card-dark: #1b1a18;
    --text-contact: #555555;
    --text-muted: #9a9a9a;
    --band-grey: #b3b3b3;
    --signature-tone: #e6e6e6;
  }
  * { box-sizing: border-box; margin: 0; padding: 0; }
  html, body { width: 1155px; height: 1200px; overflow: hidden; }
  body { background: var(--backdrop); position: relative; font-family: "Lato", sans-serif; }

  .icon-defs { position: absolute; width: 0; height: 0; }

  /* ---------- Letterhead ---------- */
  .letterhead {
    position: absolute; left: 36px; top: 101px;
    width: 706px; height: 998px; background: var(--paper);
  }
  .brand { position: absolute; display: flex; align-items: center; }
  .brand-square { background: var(--ink); flex: none; }
  .brand-name {
    font-family: "Lato", sans-serif; font-weight: 400; text-transform: uppercase;
    color: var(--ink); line-height: 1.05; letter-spacing: .01em; white-space: nowrap;
  }
  .letterhead .brand { left: 46px; top: 67px; }
  .letterhead .brand-square { width: 58px; height: 58px; margin-right: 10px; }
  .letterhead .brand-name { font-size: 19px; }

  .contact-list { position: absolute; list-style: none; color: var(--text-contact); }
  .contact-list li { display: flex; align-items: flex-start; white-space: nowrap; }
  .contact-icon { flex: none; }
  .letterhead .contact-list { left: 512px; top: 49px; font-size: 9.6px; line-height: 12px; }
  .letterhead .contact-list li { margin-bottom: 7.5px; }
  .letterhead .contact-list li:first-child { margin-bottom: 10px; }
  .letterhead .contact-icon { width: 12px; height: 12px; margin-right: 5px; }

  .recipient { position: absolute; left: 46px; top: 267px; font-family: "Questrial", sans-serif; color: var(--text-muted); }
  .recipient-name { font-family: "Montserrat", sans-serif; font-weight: 600; font-size: 21px; color: var(--ink); margin-bottom: 6px; }
  .recipient p { font-size: 12.4px; line-height: 17px; margin-bottom: 6px; }
  .recipient p.address { margin-bottom: 0; }

  .letter-body p {
    position: absolute; left: 46px; width: 612px;
    font-family: "Questrial", sans-serif; font-size: 15.3px; line-height: 22px;
    color: var(--text-muted);
  }
  .letter-body .para-1 { top: 412px; }
  .letter-body .para-2 { top: 588px; }
  .letter-body .para-3 { top: 698px; }

  .sign-off { position: absolute; right: 49px; top: 790px; font-family: "Montserrat", sans-serif; font-weight: 600; font-size: 14.7px; color: var(--ink); }
  .signature { position: absolute; left: 520px; top: 827px; width: 100px; height: 64px; background: var(--signature-tone); }

  .footer-band { position: absolute; left: 0; bottom: 32px; width: 100%; height: 9px; }

  /* ---------- Business cards ---------- */
  .card { position: absolute; left: 780px; width: 343px; height: 213px; }
  .card-front { top: 283px; background: var(--paper); }
  .card-back { top: 530px; background: var(--card-dark); }

  .card-front .brand { left: 22px; top: 85px; }
  .card-front .brand-square { width: 36px; height: 36px; margin-right: 7px; }
  .card-front .brand-name { font-size: 11px; }

  .cardholder { position: absolute; left: 177px; top: 40px; }
  .cardholder-name { font-family: "Lato", sans-serif; font-weight: 900; font-size: 11px; color: var(--ink); letter-spacing: .02em; }
  .cardholder-title { font-size: 8.6px; color: var(--text-contact); margin-top: 1px; }
  .cardholder-rule { width: 30px; height: 1.5px; background: var(--ink); margin-top: 4px; }

  .card-front .contact-list { left: 177px; top: 81px; font-size: 7.6px; line-height: 9.8px; }
  .card-front .contact-list li { margin-bottom: 6.5px; }
  .card-front .contact-icon { width: 10px; height: 10px; margin-right: 3px; }

  .card-front .footer-band { bottom: 23px; height: 7px; }

  .card-back .brand { left: 93px; top: 80px; }
  .card-back .brand-square { width: 53px; height: 53px; border: 1.2px solid var(--paper); margin-right: 9px; }
  .card-back .brand-name { font-size: 17px; color: var(--paper); }
</style>
</head>
<body>

<svg class="icon-defs" aria-hidden="true">
  <symbol id="icon-pin" viewBox="0 0 12 12">
    <rect width="12" height="12" fill="#111"/>
    <path d="M6 2.2a2.6 2.6 0 0 0-2.6 2.6C3.4 6.8 6 9.8 6 9.8s2.6-3 2.6-5A2.6 2.6 0 0 0 6 2.2z" fill="#fff"/>
    <circle cx="6" cy="4.8" r="1" fill="#111"/>
  </symbol>
  <symbol id="icon-phone" viewBox="0 0 12 12">
    <rect width="12" height="12" fill="#111"/>
    <path d="M3.6 2.3l1.3 1.9-.8.9c.5 1.1 1.3 1.9 2.4 2.5l.9-.8 1.9 1.3-.6 1.5c-3.2-.2-6.3-3.3-6.5-6.5z" fill="#fff"/>
  </symbol>
  <symbol id="icon-mail" viewBox="0 0 12 12">
    <rect width="12" height="12" fill="#111"/>
    <rect x="2.3" y="3.4" width="7.4" height="5.2" fill="none" stroke="#fff" stroke-width=".9"/>
    <path d="M2.3 3.4L6 6.6l3.7-3.2M2.3 8.6l2.6-2.6M9.7 8.6L7.1 6" fill="none" stroke="#fff" stroke-width=".8"/>
  </symbol>
  <symbol id="icon-pointer" viewBox="0 0 12 12">
    <rect width="12" height="12" fill="#111"/>
    <path d="M3.6 2.4l5 4.3-2.2.2 1.3 2.6-1 .5-1.3-2.6-1.7 1.5z" fill="#fff"/>
  </symbol>
</svg>

<main class="letterhead">
  <header>
    <div class="brand">
      <span class="brand-square"></span>
      <span class="brand-name">Halloran<br>Brightmoor PC</span>
    </div>
    <ul class="contact-list">
      <li><svg class="contact-icon"><use href="#icon-pin"/></svg><span>M. Dana Whitcombe, Esq. | President<br>4180 Larkspur Ave. | suite 600<br>Fairmont Hills, CA 90415</span></li>
      <li><svg class="contact-icon"><use href="#icon-phone"/></svg><span>(855) 555-0147</span></li>
      <li><svg class="contact-icon"><use href="#icon-mail"/></svg><span>dana@halloranbrightmoor.com</span></li>
      <li><svg class="contact-icon"><use href="#icon-pointer"/></svg><span>www.halloranbrightmoor.com</span></li>
    </ul>
  </header>

  <section class="recipient">
    <h2 class="recipient-name">Jone Smith</h2>
    <p>0123-456-789</p>
    <p>info@youremailaddress.com</p>
    <p class="address">1234 City Your Ln. Suite<br>123 Dallas, TX 0000</p>
  </section>

  <section class="letter-body">
    <p class="para-1">Lorem ipsum dolor sit amet, consectetuer adipiscing elit, sed diam nonummy nibh euismod tincidunt ut laoreet dolore magna aliquam erat volutpat. Ut wisi enim ad minim veniam, quis nostrud exerci tation ullamcorper suscipit lobortis nisl ut aliquip ex ea commodo consequat. Duis autem vel eum iriure dolor in hendrerit in vulputate velit esse molestie consequat, vel illum dolore eu feugiat nulla facilisis at vero eros et accumsan et iusto odio dignissim qui blandit praesent luptatum zzril delenit augue duis dolore te feugait nulla facilisi.</p>
    <p class="para-2">Lorem ipsum dolor sit amet, cons ectetuer adipiscing elit, sed diam nonummy nibh euismod tincidunt ut laoreet dolore magna aliquam erat volutpat. Ut wisi enim ad minim veniam, quis nostrud exerci tation ullamcorper suscipit lobortis nisl ut aliquip ex ea commodo consequat.</p>
    <p class="para-3">Lorem ipsum dolor sit amet, consectetuer adipiscing elit, sed diam nonummy nibh euismod tincidunt ut laoreet dolore magna aliquam erat</p>
  </section>

  <p class="sign-off">Mr. Graham T. Ellery</p>
  <div class="signature" role="img" aria-label="Handwritten signature of Graham T. Ellery"></div>

  <svg class="footer-band" viewBox="0 0 706 9" preserveAspectRatio="none" aria-hidden="true">
    <rect x="0" y="5" width="398" height="4" fill="var(--band-grey)"/>
    <polygon points="408,0 706,0 706,9 400,9" fill="var(--ink)"/>
  </svg>
</main>

<section class="card card-front">
  <div class="brand">
    <span class="brand-square"></span>
    <span class="brand-name">Halloran<br>Brightmoor PC</span>
  </div>
  <div class="cardholder">
    <h3 class="cardholder-name">GRAHAM T. ELLERY</h3>
    <p class="cardholder-title">Managing Director</p>
    <div class="cardholder-rule"></div>
  </div>
  <ul class="contact-list">
    <li><svg class="contact-icon"><use href="#icon-pin"/></svg><span>M. Dana Whitcombe, Esq. | President<br>4180 Larkspur Ave. | suite 600<br>Fairmont Hills, CA 90415</span></li>
    <li><svg class="contact-icon"><use href="#icon-phone"/></svg><span>(855) 555-0147</span></li>
    <li><svg class="contact-icon"><use href="#icon-mail"/></svg><span>dana@halloranbrightmoor.com</span></li>
    <li><svg class="contact-icon"><use href="#icon-pointer"/></svg><span>www.halloranbrightmoor.com</span></li>
  </ul>
  <svg class="footer-band" viewBox="0 0 343 7" preserveAspectRatio="none" aria-hidden="true">
    <rect x="0" y="4" width="168" height="3" fill="var(--band-grey)"/>
    <polygon points="174,0 343,0 343,7 168,7" fill="var(--ink)"/>
  </svg>
</section>

<section class="card card-back">
  <div class="brand">
    <span class="brand-square"></span>
    <span class="brand-name">Halloran<br>Brightmoor PC</span>
  </div>
</section>

</body>
</html>
```